Property risk and finance brokerage company needs a business card design

Tarn Financial requires a business card design. Please integrate existing logo (refer uploaded file).
hex codes used on logo #002649 #008ED6 #444F51 #ADAFAA
font used - Cinzel
Contact information
Roslyn Venterelli
Director
Mobile: 0471 385 902
email: r.venterelli@tarnfinancial.com.au
website: www.tarnfinancial.com.au
CRN : 815390
PO Box 547
Larchmere, Victoria, 3258
Horizontal orientation please

```html
<!DOCTYPE html>
<html lang="en">
<head>
<meta charset="utf-8">
<title>Tarn Financial – Business Card</title>
<link rel="stylesheet" href="https://fonts.googleapis.com/css2?family=Cinzel:wght@400;600&family=EB+Garamond:wght@400;500&display=swap">
<style>
  :root {
    --navy: #002649;
    --blue: #008ED6;
    --slate: #444F51;
    --silver: #ADAFAA;
    --card-white: #EDEEEE;
    --backdrop: #D9D6D0;
  }
  * { box-sizing: border-box; margin: 0; padding: 0; }
  html, body { width: 1200px; height: 900px; overflow: hidden; }
  body {
    background: var(--backdrop);
    position: relative;
    font-family: "EB Garamond", Georgia, serif;
  }
  .card {
    position: absolute;
    width: 560px;
    height: 320px;
    border-radius: 3px;
    box-shadow: 0 10px 24px rgba(0,0,0,0.22);
    overflow: hidden;
  }
  .card--front { left: 120px; top: 90px; background: var(--navy); }
  .card--back  { left: 520px; top: 490px; background: var(--card-white); }

  .brand { display: flex; align-items: center; gap: 16px; font-family: "Cinzel", serif; font-weight: 600; }
  .brand__dot { width: 54px; height: 54px; border-radius: 50%; background: var(--blue); flex: none; }
  .brand__name { line-height: 0.9; }
  .brand__word { display: block; font-size: 48px; letter-spacing: 1px; }
  .brand__sub  { display: block; font-size: 22px; letter-spacing: 3px; margin-top: 4px; }

  .card--front .brand { position: absolute; left: 50%; top: 50%; transform: translate(-50%, -50%); color: var(--silver); }

  .edge-band { position: absolute; left: 0; top: 0; bottom: 0; width: 34px; background: var(--navy); }
  .edge-band::after { content: ""; position: absolute; right: 0; top: 0; bottom: 0; width: 12px; background: var(--blue); }

  .holder { position: absolute; left: 62px; top: 42px; color: var(--slate); }
  .holder__name { font-size: 24px; letter-spacing: 0.5px; }
  .holder__title { font-family: "Cinzel", serif; font-size: 12px; letter-spacing: 1px; margin-top: 2px; }

  .contact { position: absolute; left: 300px; top: 30px; list-style: none; color: var(--slate); font-size: 13.5px; line-height: 19px; }
  .contact li { display: flex; align-items: center; gap: 7px; white-space: nowrap; }
  .contact svg { width: 11px; height: 11px; flex: none; fill: var(--slate); }
  .contact .plain { padding-left: 18px; }

  .card--back .brand { position: absolute; right: 46px; bottom: 44px; color: var(--navy); }
</style>
</head>
<body>
  <section class="card card--front" aria-label="Card front">
    <div class="brand">
      <span class="brand__dot"></span>
      <span class="brand__name"><span class="brand__word">TARN</span><span class="brand__sub">FINANCIAL</span></span>
    </div>
  </section>

  <section class="card card--back" aria-label="Card back">
    <div class="edge-band"></div>
    <div class="holder">
      <p class="holder__name">Roslyn Venterelli</p>
      <p class="holder__title">MANAGING DIRECTOR</p>
    </div>
    <ul class="contact">
      <li><svg viewBox="0 0 12 12" aria-hidden="true"><rect x="3" y="0.5" width="6" height="11" rx="1"/><rect x="4" y="1.8" width="4" height="7" fill="#EDEEEE"/></svg>0471 385 902</li>
      <li><svg viewBox="0 0 12 12" aria-hidden="true"><rect x="0.5" y="2" width="11" height="8"/><path d="M1 2.5 6 6.5 11 2.5" stroke="#EDEEEE" stroke-width="1" fill="none"/></svg>r.venterelli@tarnfinancial.com.au</li>
      <li><svg viewBox="0 0 12 12" aria-hidden="true"><circle cx="6" cy="6" r="5.5"/><path d="M0.5 6h11M6 0.5c-3 3-3 8 0 11M6 0.5c3 3 3 8 0 11" stroke="#EDEEEE" stroke-width="0.8" fill="none"/></svg>www.tarnfinancial.com.au</li>
      <li class="plain">PO Box 547</li>
      <li class="plain">Larchmere, Victoria, 3258</li>
      <li class="plain">Credit Rep No.: nnn nnn nnn</li>
    </ul>
    <div class="brand">
      <span class="brand__dot"></span>
      <span class="brand__name"><span class="brand__word">TARN</span><span class="brand__sub">FINANCIAL</span></span>
    </div>
  </section>
</body>
</html>
```